4 'Thank you' greetings cards designs

We are a small greetings card publisher and we need designs for a range of 'Thank you' greetings cards and notecards.
This project is for a total of 4 designs.
Please take a look at this board on Moodpinly, to see the kind of thing we are looking for: https://www.moodpinly.example/dorvek481/thank-you-cards/
The cards will be printed at a maximum size of 131mm x 183mm (including a 3mm bleed) so please provide 300dpi CMYK files at this size. Please ensure that any text (or elements of the design that are not part of the bleed) are at least 11mm in from each edge. Also, please note that cards do not have to have a bleed if your design doesn't require it (e.g. a plain white background).
Please provide 2 designs in 'portrait' orientation and 2 in 'landscape'.
Please provide 2 designs that just have the words 'Thank you' and then 2 designs that include your choice of these alternative messages:
Thank you so much
Thanks very much
Thank you very much
Thanks a million
Just to say thank you
A big thank you
A really big thank you
Feel free to use an exclamation mark on a couple of your designs, if you wish!
Other than the above guidelines, everything else is up to you in terms of colours, fonts, shapes, etc. - but please use the Moodpinly board to see the kind of designs we are looking for.
Thank you!

```html
<!DOCTYPE html>
<html lang="en">
<head>
<meta charset="utf-8">
<title>Thank You Card</title>
<link rel="stylesheet" href="https://fonts.googleapis.com/css2?family=Anton&display=swap">
<style>
  :root {
    --paper: #ffffff;
    --lavender: #d8def8;
    --periwinkle: #b4bdf0;
    --ice: #cdf1f5;
    --aqua: #9fe3ea;
    --mint: #92dcc0;
    --orchid: #f09cf2;
    --orchid-soft: #f4bff4;
    --violet: #8b7fe0;
    --royal: #2f5ade;
  }
  html, body {
    margin: 0;
    padding: 0;
    width: 941px;
    height: 1200px;
    overflow: hidden;
    background: var(--paper);
  }
  .card {
    display: block;
    width: 941px;
    height: 1200px;
  }
  .greeting {
    font-family: 'Anton', 'Oswald', sans-serif;
  }
  .tone-lavender { fill: var(--lavender); }
  .tone-periwinkle { fill: var(--periwinkle); }
  .tone-ice { fill: var(--ice); }
  .tone-aqua { fill: var(--aqua); }
  .tone-mint { fill: var(--mint); }
  .tone-orchid { fill: var(--orchid); }
  .tone-orchid-soft { fill: var(--orchid-soft); }
  .tone-violet { fill: var(--violet); }
  .tone-royal { fill: var(--royal); }
  .heart-pink { fill: var(--orchid); }
  .heart-lavender { fill: var(--lavender); opacity: 0.9; }
  .heart-small-lavender { fill: var(--periwinkle); opacity: 0.55; }
  .heart-small-ice { fill: var(--ice); opacity: 0.75; }
</style>
</head>
<body>
<svg class="card" viewBox="0 0 928 1297" preserveAspectRatio="none" xmlns="http://www.w3.org/2000/svg" role="img" aria-label="Thank You card with overlapping hearts">
  <defs>
    <path id="heart" d="M50 96 C35 80 0 60 0 30 C0 12 13 0 28 0 C40 0 47 8 50 16 C53 8 60 0 72 0 C87 0 100 12 100 30 C100 60 65 80 50 96 Z"/>
  </defs>
  <rect width="928" height="1297" fill="var(--paper)"/>

  <g class="border-words greeting">
    <text class="tone-lavender" x="9" y="220" font-size="460" textLength="1040" lengthAdjust="spacingAndGlyphs">Thank You</text>
    <text class="tone-lavender" x="129" y="1510" font-size="470" textLength="1010" lengthAdjust="spacingAndGlyphs">Thank You</text>
    <text class="tone-ice" transform="translate(0 309) rotate(90)" x="0" y="0" font-size="114" textLength="435" lengthAdjust="spacingAndGlyphs">Thank You</text>
    <text class="tone-periwinkle" transform="translate(0 844) rotate(90)" x="0" y="0" font-size="108" textLength="400" lengthAdjust="spacingAndGlyphs">Thank You</text>
    <text class="tone-periwinkle" transform="translate(824 194) rotate(90)" x="0" y="0" font-size="118" textLength="390" lengthAdjust="spacingAndGlyphs">Thank You</text>
    <text class="tone-ice" transform="translate(839 564) rotate(90)" x="0" y="0" font-size="100" textLength="435" lengthAdjust="spacingAndGlyphs">Thank You</text>
  </g>

  <g class="upper-words greeting">
    <text class="tone-orchid-soft" x="182" y="254" font-size="104" textLength="287" lengthAdjust="spacingAndGlyphs" opacity="0.85">Thank You</text>
    <text class="tone-ice" x="354" y="369" font-size="150" textLength="450" lengthAdjust="spacingAndGlyphs">Thank You</text>
    <text class="tone-orchid" x="479" y="244" font-size="138" textLength="365" lengthAdjust="spacingAndGlyphs" opacity="0.95">Thank You</text>
    <use href="#heart" class="heart-pink" transform="translate(129 209) scale(1.15 0.89)" opacity="0.9"/>
    <use href="#heart" class="heart-small-lavender" transform="translate(194 224) scale(0.88 0.94)"/>
    <text class="tone-periwinkle" x="79" y="319" font-size="67" textLength="175" lengthAdjust="spacingAndGlyphs">Thank You</text>
  </g>

  <g class="centre-hearts">
    <use href="#heart" class="heart-pink" transform="translate(182 429) scale(5.14 5.1)"/>
    <use href="#heart" class="heart-lavender" transform="translate(464 530) scale(3.45 3.96)"/>
  </g>

  <g class="centre-words greeting">
    <text class="tone-royal" x="132" y="734" font-size="236" textLength="662" lengthAdjust="spacingAndGlyphs">Thank You</text>
    <text class="tone-mint" x="136" y="519" font-size="29" textLength="80" lengthAdjust="spacingAndGlyphs">Thank You</text>
    <text class="tone-mint" x="560" y="519" font-size="29" textLength="80" lengthAdjust="spacingAndGlyphs">Thank You</text>
    <text class="tone-aqua" x="278" y="569" font-size="52" textLength="128" lengthAdjust="spacingAndGlyphs">Thank You</text>
    <text class="tone-periwinkle" x="679" y="567" font-size="52" textLength="128" lengthAdjust="spacingAndGlyphs">Thank You</text>
    <text class="tone-orchid" transform="translate(126 724) rotate(-90)" x="0" y="0" font-size="65" textLength="180" lengthAdjust="spacingAndGlyphs">Thank You</text>
    <text class="tone-aqua" transform="translate(794 589) rotate(90)" x="0" y="0" font-size="46" textLength="130" lengthAdjust="spacingAndGlyphs">Thank You</text>
    <text class="tone-mint" x="106" y="789" font-size="58" textLength="158" lengthAdjust="spacingAndGlyphs">Thank You</text>
    <text class="tone-violet" x="286" y="791" font-size="62" textLength="182" lengthAdjust="spacingAndGlyphs">Thank You</text>
    <text class="tone-aqua" x="474" y="786" font-size="48" textLength="128" lengthAdjust="spacingAndGlyphs">Thank You</text>
    <text class="tone-orchid" x="606" y="794" font-size="66" textLength="176" lengthAdjust="spacingAndGlyphs">Thank You</text>
  </g>

  <g class="lower-words greeting">
    <text class="tone-ice" x="399" y="1139" font-size="172" textLength="465" lengthAdjust="spacingAndGlyphs">Thank You</text>
    <text class="tone-orchid-soft" x="139" y="1174" font-size="115" textLength="290" lengthAdjust="spacingAndGlyphs">Thank You</text>
    <text class="tone-periwinkle" x="664" y="1006" font-size="66" textLength="175" lengthAdjust="spacingAndGlyphs">Thank You</text>
    <use href="#heart" class="heart-pink" transform="translate(719 1007) scale(1.2 1.1)" opacity="0.85"/>
    <use href="#heart" class="heart-small-ice" transform="translate(764 1019) scale(1.05 1.0)"/>
  </g>
</svg>
</body>
</html>
```